Brightwave Travel and Tours

Hotel Reservations
Airline Ticketing
Day Tour

My business is a Travel agency. My services are issuing domestic and international tickets. Book room/hotel reservations local/international.
My color preference is apple green/orange/red/blue.
Images of beaches, tickets,luggage.

```html
<!DOCTYPE html>
<html lang="en">
<head>
<meta charset="utf-8">
<title>Brightwave Travel and Tours – Business Card</title>
<link href="https://fonts.googleapis.com/css2?family=Lato:wght@400;700&display=swap" rel="stylesheet">
<style>
  :root {
    --backdrop-light: #e6e6e6;
    --backdrop-dark: #c9c9c9;
    --kraft: #c6a87c;
    --kraft-light: #d2b68c;
    --card-edge: #232323;
    --brand-blue: #1a8fc2;
    --ink: #111111;
  }
  * { box-sizing: border-box; margin: 0; padding: 0; }
  html, body { width: 1200px; height: 899px; overflow: hidden; }
  body {
    background: linear-gradient(90deg, var(--backdrop-light), var(--backdrop-dark));
    font-family: "Lato", Arial, sans-serif;
    color: var(--ink);
    position: relative;
  }
  .card {
    position: absolute;
    left: 370px;
    width: 460px;
    height: 262px;
    border: 8px solid var(--card-edge);
    background: radial-gradient(circle at 50% 40%, var(--kraft-light), var(--kraft));
    box-shadow: 0 6px 14px rgba(0,0,0,0.18);
  }
  .card--front { top: 150px; }
  .card--back { top: 450px; }

  .brand {
    position: absolute;
    inset: 0;
    display: flex;
    flex-direction: column;
    align-items: center;
    justify-content: center;
    gap: 14px;
  }
  .brand__dot {
    width: 70px;
    height: 70px;
    border-radius: 50%;
    background: var(--brand-blue);
  }
  .brand__name {
    font-weight: 700;
    font-size: 24px;
    color: var(--brand-blue);
    letter-spacing: 0.5px;
    white-space: nowrap;
  }

  .contact {
    position: absolute;
    left: 50px;
    top: 58px;
  }
  .contact__name { font-size: 20px; font-weight: 400; line-height: 1.1; }
  .contact__name strong { font-weight: 700; }
  .contact__role { font-size: 13px; letter-spacing: 0.5px; margin-bottom: 16px; }
  .contact__address { font-size: 13px; font-weight: 700; line-height: 1.35; margin-bottom: 18px; }
  .contact__list { list-style: none; font-size: 14px; line-height: 1.55; }
  .contact__list li { display: flex; align-items: center; gap: 12px; white-space: nowrap; }
  .contact__list svg { width: 12px; height: 12px; flex: none; }
</style>
</head>
<body>
  <section class="card card--front" aria-label="Card front">
    <div class="brand">
      <div class="brand__dot"></div>
      <div class="brand__name">Brightwave Travel and Tours</div>
    </div>
  </section>

  <section class="card card--back" aria-label="Card back">
    <div class="contact">
      <p class="contact__name">Clara <strong>Mendez</strong></p>
      <p class="contact__role">MANAGER</p>
      <p class="contact__address">Address Line 1<br>Address Line 2</p>
      <ul class="contact__list">
        <li>
          <svg viewBox="0 0 12 12" aria-hidden="true"><path fill="#111" d="M1 4.5 Q6 0.5 11 4.5 L9.5 5.8 L8.2 4.6 H3.8 L2.5 5.8 Z M2.5 6.5 H9.5 L10 11 H2 Z"/></svg>
          555 204 318
        </li>
        <li>
          <svg viewBox="0 0 12 12" aria-hidden="true"><path d="M0.6 2.5 H11.4 V9.5 H0.6 Z M0.8 2.8 L6 7 L11.2 2.8" fill="none" stroke="#111" stroke-width="1.2"/></svg>
          desk@brightwave.com
        </li>
        <li>
          <svg viewBox="0 0 12 12" aria-hidden="true"><circle cx="6" cy="6" r="5" fill="none" stroke="#111" stroke-width="1.2"/><path d="M1 6 H11 M6 1 V11" stroke="#111" stroke-width="1"/></svg>
          www.brightwave.com
        </li>
      </ul>
    </div>
  </section>
</body>
</html>
```